SkyvoraQ Business Cards and Stationary Design

Need a design for our business cards and stationary. I want to carry on the theme of the logo. I want the business cards to have a design on the back. I would like the business cards and the stationary to carry the same theme, design scheme, and branding

Target Market(s)

Airlines and Maintenance Facilities

Industry/Entity Type

Aviation

Contact Information for Business Card

Name
Position Title
Address: 4827 Tollbeck Lane, Marlow Bay, Delvara, 58213
Office Number
Mobile Number
Email
Website

Font styles to use
Serif
Sans Serif

Colors

Designer to choose colors to be used in the design.

```html
<!DOCTYPE html>
<html lang="en">
<head>
<meta charset="utf-8">
<title>SkyvoraQ Business Card</title>
<link rel="stylesheet" href="https://fonts.googleapis.com/css2?family=Open+Sans:wght@400;600;700&display=swap">
<style>
  :root {
    --bg: #dcdcdc;
    --paper: #f7f7f7;
    --navy: #13305a;
    --ink: #2a2f38;
    --accent: #1f86c2;
    --blue-top: #2386bd;
    --blue-bottom: #102e57;
    --silver: #c9ced6;
  }
  * { margin: 0; padding: 0; box-sizing: border-box; }
  html, body {
    width: 1200px; height: 835px; overflow: hidden;
    background: var(--bg);
    font-family: "Open Sans", Arial, sans-serif;
  }
  .canvas {
    width: 1200px; height: 835px;
    display: flex; align-items: center; justify-content: center; gap: 60px;
  }
  .card {
    width: 520px; height: 300px;
    border-radius: 4px;
    box-shadow: 0 6px 18px rgba(0,0,0,0.18);
    position: relative;
    overflow: hidden;
  }
  .card-front { background: var(--paper); }
  .brand {
    position: absolute; left: 36px; top: 34px;
    display: flex; align-items: center; gap: 10px;
  }
  .brand-name {
    font-weight: 700; font-size: 22px; letter-spacing: 4px;
    color: var(--navy); text-transform: uppercase;
  }
  .brand-dot {
    width: 26px; height: 26px; border-radius: 50%;
    background: var(--accent);
  }
  .contact {
    position: absolute; right: 34px; bottom: 30px;
    text-align: right; color: var(--ink);
  }
  .person-name {
    font-weight: 700; font-size: 19px; letter-spacing: 1px;
    color: var(--navy); text-transform: uppercase; line-height: 1.1;
  }
  .person-title { font-size: 12px; margin-bottom: 10px; }
  .contact-line {
    display: flex; justify-content: flex-end; align-items: center; gap: 8px;
    font-size: 11.5px; line-height: 17px;
  }
  .contact-line svg { width: 11px; height: 11px; fill: var(--accent); flex: none; }
  .contact-line.no-icon { padding-right: 19px; }
  .card-back {
    background: linear-gradient(160deg, var(--blue-top), var(--blue-bottom));
    display: flex; align-items: center; justify-content: center; gap: 14px;
  }
  .back-ring {
    width: 60px; height: 60px; border-radius: 50%;
    border: 6px solid var(--silver);
  }
  .back-name {
    font-weight: 700; font-size: 30px; letter-spacing: 5px;
    color: var(--silver); text-transform: uppercase;
  }
</style>
</head>
<body>
<main class="canvas">
  <section class="card card-front">
    <div class="brand">
      <span class="brand-name">SkyvoraQ</span>
      <span class="brand-dot"></span>
    </div>
    <div class="contact">
      <div class="person-name">Marlo Denvik</div>
      <div class="person-title">Director Technical</div>
      <div class="contact-line">555 218 4407
        <svg viewBox="0 0 12 12"><rect x="3" y="0.5" width="6" height="11" rx="1.2"/></svg></div>
      <div class="contact-line">555 218 4410
        <svg viewBox="0 0 12 12"><path d="M2.5 1 L4.5 1 L5.5 3.5 L4.2 4.5 Q5.2 6.8 7.5 7.8 L8.5 6.5 L11 7.5 L11 9.5 Q10.5 11 9 11 Q1 9.5 1 2.5 Q1 1 2.5 1Z"/></svg></div>
      <div class="contact-line">info@skyvoraq.com
        <svg viewBox="0 0 12 12"><rect x="0.5" y="2.5" width="11" height="7.5" rx="1"/></svg></div>
      <div class="contact-line">www.skyvoraq.com
        <svg viewBox="0 0 12 12"><circle cx="6" cy="6" r="5.5"/></svg></div>
      <div class="contact-line">4827 Tollbeck Lane, Marlow Bay
        <svg viewBox="0 0 12 12"><path d="M6 0.5 A4 4 0 0 1 10 4.5 Q10 7 6 11.5 Q2 7 2 4.5 A4 4 0 0 1 6 0.5Z"/></svg></div>
      <div class="contact-line no-icon">Delvara, 58213</div>
    </div>
  </section>
  <section class="card card-back">
    <span class="back-ring"></span>
    <span class="back-name">SkyvoraQ</span>
  </section>
</main>
</body>
</html>
```